Beautiful e-comm site for 'roadside farmers stand' online!

Need a logo design and basic e-comm website (super super simple) for new business called Brambletoft. Brambletoft is an online farmers stand where local artisans can sell 'brambletoft' goods directly from their makers!

Looking for something simple, whimsicle and clean! (Ideally with a light grey or perrywinkle and some color mixed in - word 'Brambletoft' in black - can work the pear shape in somewhere but not required!)

Target Market(s)

Hobby shoppers and 'quilo' goers who want a focus on edible things and care about ingredients!

Industry/Entity Type

E-Commerce

Number of Pages Required

2 page

Font styles to use
Decorative
Script

Colors
f3f1f8
ec1f27
cadf82

Requirements
Must have
• - Basic logo
• - Homepage
• - Product Detail Page
• - Be in a responsive, woocommerce or shopify, wordpress theme (will purchase theme after design is approved)
Nice to have
• - Matching check out & cart pages
• - 'About Us' page
• - SEO plugin
Should not have
• A cluttered look/feel.

```html
<!DOCTYPE html>
<html lang="en">
<head>
<meta charset="utf-8">
<title>Brambletoft — Grapefruit Insect repellant</title>
<link href="https://fonts.googleapis.com/css2?family=Bitter:wght@700&family=Lato:wght@300;400;700&display=swap" rel="stylesheet">
<style>
:root{
  --page:#f3f1f8;
  --white:#ffffff;
  --green:#1f9a3a;
  --green-dark:#1c8a1c;
  --lime:#8dc63f;
  --red:#ec1f27;
  --ink:#333333;
  --muted:#666666;
  --link:#6a6ad8;
  --star:#f5c518;
  --rule:#d4d2da;
  --footer:#0e2a10;
  --logo:#222222;
}
*{margin:0;padding:0;box-sizing:border-box}
html,body{width:1200px;height:2817px;overflow:hidden}
body{background:var(--page);font-family:'Lato',sans-serif;color:var(--ink);position:relative}
.abs{position:absolute}

/* header */
.site-header{left:0;top:0;width:1200px;height:75px;background:var(--white)}
.logo{left:178px;top:18px;font:700 34px/40px 'Lato',sans-serif;color:var(--logo);display:flex;align-items:center;gap:10px}
.logo-dot{width:14px;height:14px;border-radius:50%;background:var(--lime)}
.nav{top:20px;font-size:14px;color:var(--muted);line-height:22px}
.nav-shop{background:var(--green);color:var(--white);border-radius:14px;padding:3px 16px;top:17px}
.cart{display:flex;align-items:center;gap:8px}

/* hero */
.hero{left:0;top:75px;width:1200px;height:530px;background:radial-gradient(ellipse at 30% 40%,#7aa64a,#3d6a2a 60%,#27401c)}
.hero-panel{left:160px;top:222px;width:573px;height:332px;background:rgba(20,30,20,.55)}
.hero-title{left:178px;top:260px;font:700 44px/54px 'Bitter',serif;color:var(--white)}
.hero-sub{left:178px;top:322px;font:400 29px/38px 'Lato',sans-serif;color:var(--white);letter-spacing:1px}
.hero-text{left:178px;top:373px;width:430px;font:700 15px/22px 'Lato',sans-serif;color:var(--white);letter-spacing:.5px}
.hero-btn{left:178px;top:443px;width:132px;height:49px;border:2px solid var(--white);color:var(--white);font:700 15px/45px 'Lato',sans-serif;text-align:center;letter-spacing:1.5px}

.section-title{left:0;width:1200px;top:668px;text-align:center;font:400 29px/36px 'Lato',sans-serif;color:var(--green)}
.breadcrumb{left:182px;top:769px;font-size:22px;line-height:28px}
.breadcrumb a{color:var(--link);text-decoration:none}

/* product */
.main-photo{left:178px;top:819px;width:489px;height:486px;border:1px solid #bbb;background:linear-gradient(180deg,#e9ecef 0%,#c8cfc9 45%,#3f6a2e 80%,#dfe4e0 100%)}
.thumb{top:1339px;width:132px;height:133px;border:2px solid #bbb;background:linear-gradient(#f4f4f4,#a0855a)}
.thumb.active{background:linear-gradient(#dfe4e0,#3f6a2e)}
.product-name{left:695px;top:818px;font:400 29px/30px 'Lato',sans-serif;color:var(--green-dark)}
.price{left:933px;top:822px;font:400 31px/36px 'Lato',sans-serif;color:var(--red)}
.old-price{left:933px;top:868px;font:700 22px/28px 'Lato',sans-serif;color:#555;text-decoration:line-through}
.stars{left:695px;top:924px;display:flex;gap:2px}
.reviews{left:854px;top:932px;font-size:14px;color:var(--link)}
.rule{height:1px;background:var(--rule)}
.stock{left:704px;top:981px;font:700 14px/20px 'Lato',sans-serif;color:var(--green-dark)}
.size-label{left:704px;top:1014px;font-size:14px}
.size-btn{top:1042px;width:122px;height:44px;border:1px solid var(--green);border-radius:6px;text-align:center;font-size:11px;line-height:15px;padding-top:7px}
.size-btn.selected{background:#d6d6d6;border-color:#999}
.qty{left:704px;top:1124px;font-size:15px;display:flex;align-items:center;gap:6px}
.qty-box{width:60px;height:24px;border:1px solid #aaa;background:var(--white);font-size:13px;padding-left:5px;line-height:22px}
.add-cart{left:695px;top:1166px;width:131px;height:42px;background:var(--green-dark);color:var(--white);font:700 14px/42px 'Lato',sans-serif;text-align:center}
.how-buy{left:866px;top:1178px;font-size:14px;color:var(--link)}

/* details */
.details-bar{left:178px;top:1538px;width:844px;height:41px;background:var(--lime);color:var(--white);font:400 14px/41px 'Lato',sans-serif;padding-left:26px}
.botanical{left:507px;top:1615px;width:207px;height:197px;background:radial-gradient(circle at 55% 40%,#ffffff,#d9d9d9 70%,var(--page))}
.intro{left:203px;top:1838px;width:805px;font-size:12px;line-height:20px;color:#444}
.detail-head{left:203px;font:700 16px/20px 'Lato',sans-serif;color:var(--green-dark)}
.detail-body{left:203px;width:805px;font-size:12px;line-height:20px;color:#444}
.detail-body.single{width:auto;white-space:nowrap}
.uses-title{left:203px;top:2232px;font:400 28px/34px 'Lato',sans-serif;color:#555}

/* promos */
.promo{top:2584px;height:109px;color:var(--white);padding:12px 14px}
.promo-dark{background:linear-gradient(90deg,#5a2a22,#3a2a28 60%,#2b2b2b)}
.promo h3{font:700 14px/18px 'Lato',sans-serif}
.promo p{font:700 10px/13px 'Lato',sans-serif;margin-top:4px;max-width:230px}
.promo a{display:inline-block;font:700 10px/12px 'Lato',sans-serif;text-decoration:underline;margin-top:10px;color:var(--white)}
.promo-wide{background:#2b2b2b;padding:0}
.promo-wide .shot{position:absolute;left:0;top:0;width:150px;height:109px;background:linear-gradient(90deg,#6d4a33,#3a2a22)}
.promo-wide .copy{position:absolute;left:142px;top:12px}
.hl{color:var(--lime)}
.promo-ship{background:#7cc576;color:var(--red);padding:10px 16px}
.promo-ship strong{display:block;font:700 34px/30px 'Lato',sans-serif}
.promo-ship span{font:700 13px/16px 'Lato',sans-serif}

.site-footer{left:0;top:2729px;width:1200px;height:88px;background:var(--footer);color:#ddd;text-align:center;font-size:14px;line-height:88px}
</style>
</head>
<body>

<header class="site-header abs">
  <div class="logo abs">Brambletoft<span class="logo-dot"></span></div>
  <span class="nav abs" style="left:476px">Home</span>
  <span class="nav abs" style="left:548px">About</span>
  <span class="nav abs" style="left:623px">Products</span>
  <span class="nav nav-shop abs" style="left:700px">Shop</span>
  <span class="nav abs" style="left:782px">Contact</span>
  <span class="nav abs" style="left:866px">Login</span>
  <span class="nav cart abs" style="left:950px">
    <svg width="18" height="16" viewBox="0 0 18 16"><path d="M0 1h3l2.5 9h9l2-6H5" fill="none" stroke="#1f9a3a" stroke-width="2"/><circle cx="7" cy="13.5" r="1.6" fill="#1f9a3a"/><circle cx="13" cy="13.5" r="1.6" fill="#1f9a3a"/></svg>
    Cart (0)
  </span>
</header>

<section class="hero abs" role="img" aria-label="Market stand crates of fresh apples, limes and melons"></section>
<div class="hero-panel abs"></div>
<h1 class="hero-title abs">Welcome to Brambletoft</h1>
<p class="hero-sub abs">Your online roadside farmer stand</p>
<p class="hero-text abs">Canned pickles, homemade jams and jellies, homemade cookies, handmade soaps and home products, etc.</p>
<div class="hero-btn abs">SHOP NOW</div>

<h2 class="section-title abs">SHOP</h2>
<nav class="breadcrumb abs"><a>Home</a> &gt; <a>Category X</a> &gt; Grapefruit Insect repellant</nav>

<div class="main-photo abs" role="img" aria-label="Amber dropper bottle of essential oil on greenery"></div>
<div class="thumb active abs" style="left:178px" role="img" aria-label="Dropper bottle thumbnail"></div>
<div class="thumb abs" style="left:321px" role="img" aria-label="Amber bottle thumbnail"></div>
<div class="thumb abs" style="left:462px" role="img" aria-label="Small bottle thumbnail"></div>

<h1 class="product-name abs">Grapefruit<br>Insect repellant</h1>
<div class="price abs">$22.00</div>
<div class="old-price abs">$25.00</div>
<div class="stars abs">
  <svg width="145" height="30" viewBox="0 0 145 30">
    <defs><path id="star" d="M14 1l4 9 9.5 1-7 6.5 2 9.5L14 22l-8.5 5 2-9.5-7-6.5 9.5-1z" fill="var(--star)"/></defs>
    <use href="#star" x="0"/><use href="#star" x="29"/><use href="#star" x="58"/><use href="#star" x="87"/><use href="#star" x="116"/>
  </svg>
</div>
<div class="reviews abs">562 Reviews | Questions</div>
<div class="rule abs" style="left:676px;top:977px;width:346px"></div>
<div class="stock abs">In Stock</div>
<div class="rule abs" style="left:676px;top:1003px;width:346px"></div>
<div class="size-label abs">Size: <b>1 fl oz</b></div>
<div class="size-btn selected abs" style="left:704px">1 fl oz<br>$22.00</div>
<div class="size-btn abs" style="left:838px">4 fl oz<br>$84.00</div>
<div class="qty abs">Quantity: <span class="qty-box">1 &nbsp;&nbsp;&nbsp;▾</span></div>
<div class="add-cart abs">Add to cart</div>
<div class="how-buy abs">How to buy?</div>

<div class="details-bar abs">Product details</div>
<div class="botanical abs" role="img" aria-label="Botanical sketch of a grapefruit with a cut wedge, labelled Grapefruit (Citrus paradisi)"></div>
<p class="intro abs">Lorem ipsum dolor sit amet, consectetur adipisicing elit, sed do eiusmod tempor incididunt ut labore et dolore magna aliqua. Ut enim ad minim veniam, quis nostrud exercitation ullamco laboris nisi ut aliquip ex ea commodo consequat. Duis aute irure dolor in reprehenderit in voluptate velit esse cillum dolore eu fugiat nulla pariatur. Excepteur sint occaecat cupidatat non proident, sunt in culpa qui officia deserunt mollit anim id est laborum.</p>

<h3 class="detail-head abs" style="top:1936px">Plant Part Used</h3>
<p class="detail-body single abs" style="top:1960px">Rind</p>
<h3 class="detail-head abs" style="top:1996px">Extraction Method</h3>
<p class="detail-body single abs" style="top:2020px">Cold-pressed</p>
<h3 class="detail-head abs" style="top:2056px">Aroma</h3>
<p class="detail-body single abs" style="top:2080px">Medium-strong strength. Tangy and sweet in aroma.</p>
<h3 class="detail-head abs" style="top:2114px">Grapefruit Essential Oil Benefits</h3>
<p class="detail-body single abs" style="top:2138px">Stimulates and refreshes the senses. Euphoria-inducing and energizing. Encouraging as it strengthens resolve. Eases occasional tension and pressure.</p>
<h3 class="detail-head abs" style="top:2174px">Blends Well With</h3>
<p class="detail-body single abs" style="top:2198px">Bergamot, Cardamom, Cypress, Geranium, Lavender, Lemon, Lime, Neroli, Patchouli, Rosemary, Sandalwood.</p>

<h2 class="uses-title abs">Aromatherapy Uses</h2>
<h3 class="detail-head abs" style="top:2279px">Bath &amp; Shower</h3>
<p class="detail-body single abs" style="top:2303px">Add 5-10 drops to hot bath water, or sprinkle into shower steam before getting in for an at-home spa experience.</p>
<h3 class="detail-head abs" style="top:2338px">Massage</h3>
<p class="detail-body abs" style="top:2362px">8-10 drops of essential oil per 1 ounce of carrier oil. Apply a small amount directly to areas of concern, such as muscles, skin or joints. Work the oil gently into the skin until it is fully absorbed.</p>
<h3 class="detail-head abs" style="top:2418px">Inhalation</h3>
<p class="detail-body single abs" style="top:2442px">Inhale the aromatic vapors directly from the bottle, or place a few drops in a burner or diffuser to fill a room with its scent.</p>
<h3 class="detail-head abs" style="top:2477px">DIY Projects</h3>
<p class="detail-body single abs" style="top:2501px">This oil can be used in your homemade DIY projects, such as in candles, soaps, and body care products!</p>

<div class="rule abs" style="left:178px;top:2548px;width:844px;background:#999"></div>

<div class="promo promo-dark abs" style="left:178px;width:203px" role="img" aria-label="Shelves of canned preserves">
  <h3>Lots of canned products</h3>
  <p>Lorem ipsum dolor sit amet, consectetur adipisicing elit, sed do</p>
  <a>SHOP NOW!</a>
</div>
<div class="promo promo-wide abs" style="left:392px;width:416px">
  <div class="shot" role="img" aria-label="Jars of homemade products on a table"></div>
  <div class="copy">
    <h3>Homemade products are truly <span class="hl">healthy</span>.</h3>
    <p>Lorem ipsum dolor sit amet, consectetur adipisicing elit, sed do eiusmod tempor incididunt ut.</p>
    <a>SHOP NOW!</a>
  </div>
</div>
<div class="promo promo-ship abs" style="left:819px;width:203px">
  <strong>FREE SHIPPING</strong>
  <span>on orders over $99.</span>
</div>

<footer class="site-footer abs">©Brambletoft All rights reserved2018</footer>

</body>
</html>
```